brightquokka.net we need a webpage designed for our new product

We need a webpage designed for our new range of products from our new brand. We have had a logo designed on sketchharbor (see attached) and we want to keep to this theme. Our first product is a range of affordable app controlled LED lightbulbs.

I have added some photos that we think is good inspirational material and would be good as a background to this website, but we want the site to look modern but not conventional. We would like something that makes our company look quirky not corporate.

Thats it

Target Market(s)

Our product is being stocked by big name online retailers in the UK, the page will get link through hits from our app. Our target market is gadget freaks of all ages.

Industry/Entity Type

It Company

Requirements
Must have
• We are going to need a help page, text to be uploaded next few days.

We need a contact page.

design my work on iOS and Android as most people will access page through their handset or tablet.
Should not have
• We do not want anything too corporate.

```html
<!DOCTYPE html>
<html lang="en">
<head>
<meta charset="utf-8">
<title>BrightQuokka — Lightbulbs</title>
<link href="https://fonts.googleapis.com/css2?family=Anton&family=Arimo:wght@400;700&display=swap" rel="stylesheet">
<style>
:root{
  --green:#3aa940;
  --green-dark:#2e8a33;
  --grey:#595959;
  --ink:#111111;
  --white:#ffffff;
  --text:#333333;
  --footer:#0d0d0d;
}
*{box-sizing:border-box;margin:0;padding:0}
html,body{width:744px;height:1200px;overflow:hidden;background:var(--white);font-family:"Arimo",Arial,sans-serif}
.page{position:relative;width:744px;height:1200px;overflow:hidden}

.hero{position:absolute;left:0;top:0;width:744px;height:380px;
  background:radial-gradient(ellipse 180px 260px at 120px 260px,#d6ebe0 0%,#a9cbbd 45%,transparent 75%),
  linear-gradient(100deg,#3f5d4f 0%,#6f8f73 30%,#2e3b2a 55%,#7f9a88 75%,#35462f 100%)}
.hero-title{position:absolute;left:0;width:744px;text-align:center;color:var(--white)}
.hero-kicker{top:200px;font-size:13px;letter-spacing:15px;padding-left:15px}
.hero-name{top:222px;font-family:"Anton",sans-serif;font-size:68px;line-height:1;text-shadow:0 2px 6px rgba(0,0,0,.35)}
.slide-arrow{position:absolute;top:190px}
.slide-arrow.prev{left:28px}
.slide-arrow.next{left:696px}

.topbar{position:absolute;left:0;top:0;width:744px;height:50px;background:var(--green);box-shadow:0 2px 4px rgba(0,0,0,.25)}
.nav a{position:absolute;top:21px;color:var(--white);font-size:10px;text-decoration:none}
.cart{position:absolute;left:576px;top:17px;display:flex;align-items:center;gap:6px;color:var(--white);font-size:14px}
.brand-badge{position:absolute;left:75px;top:5px;width:132px;height:132px;border-radius:50%;background:var(--white);
  box-shadow:0 2px 6px rgba(0,0,0,.3);display:flex;align-items:center;justify-content:center;
  color:var(--green);font-weight:700;font-size:12px}

.promo{position:absolute;top:403px;width:295px;height:146px;overflow:hidden;color:var(--white);font-weight:700}
.promo-quality{left:74px;background:var(--green)}
.promo-range{left:375px;background:var(--grey)}
.promo .photo{position:absolute;top:0;right:0;width:160px;height:146px;clip-path:polygon(40px 0,100% 0,100% 100%,0 100%)}
.promo-quality .photo{background:linear-gradient(160deg,#3a6fa8 0%,#d98a1e 40%,#6b3a1c 100%)}
.promo-range .photo{background:linear-gradient(150deg,#a22 0%,#3a4b86 45%,#8a6a4a 100%)}
.promo .copy{position:absolute;left:14px;top:12px;font-size:17px;line-height:23px}
.promo .accent{font-family:"Anton",sans-serif;font-weight:400;font-size:17px}
.promo .price{font-size:28px;color:var(--green-dark);margin-top:6px;font-weight:700}
.promo .big{font-family:"Anton",sans-serif;font-weight:400;font-size:32px;line-height:36px}

.contact{position:absolute;left:0;top:576px;width:744px;height:319px;
  background:linear-gradient(180deg,#8d8d8d 0%,#a9a9a9 40%,#7a7a7a 80%,#4e7b4d 100%)}
.contact-glow{position:absolute;left:0;bottom:0;width:744px;height:80px;
  background:radial-gradient(circle at 40px 90px,rgba(58,169,64,.75) 55px,transparent 57px),
  radial-gradient(circle at 700px 80px,rgba(58,169,64,.7) 60px,transparent 62px),
  linear-gradient(180deg,transparent 0%,rgba(58,169,64,.55) 100%)}
.contact h2{position:absolute;top:30px;left:0;width:744px;text-align:center;font-family:"Anton",sans-serif;font-weight:400;
  font-size:50px;color:var(--white);text-shadow:0 2px 4px rgba(0,0,0,.3)}
.field{position:absolute;background:var(--white);color:var(--text);font-size:9px;font-weight:700;padding:10px 12px}
.field.short{top:106px;height:29px;width:174px}
.field.message{left:99px;top:147px;width:546px;height:99px}
.send{position:absolute;left:99px;top:257px;width:546px;height:24px;background:var(--ink);color:var(--white);
  font-size:9px;display:flex;align-items:center;justify-content:center;border-bottom:2px solid var(--green)}

.product{position:absolute;top:926px;width:143px;height:184px;border:1px solid #eeeeee;background:var(--white)}
.product .shot{position:absolute;left:5px;top:4px;width:132px;height:136px;
  background:radial-gradient(ellipse 45px 40px at 60px 85px,#f4e6d8 0%,#e6cdb8 60%,transparent 75%),
  linear-gradient(180deg,#6d6a78 0%,#8a5a3a 60%,#3a2417 100%)}
.product .name{position:absolute;left:6px;top:146px;font-size:8px;color:var(--text)}
.product .cost{position:absolute;left:6px;top:157px;font-size:10px;font-weight:700;color:var(--green)}
.product .add{position:absolute;left:108px;top:143px;width:27px;height:27px;border-radius:50%;background:var(--green);
  display:flex;align-items:center;justify-content:center}

.footer{position:absolute;left:0;top:1140px;width:744px;height:60px;background:var(--footer)}
.footer .brand{position:absolute;left:85px;top:12px;color:var(--green);font-weight:700;font-size:15px;letter-spacing:1px}
.footer .legal{position:absolute;left:85px;top:35px;color:var(--white);font-size:9px}
.social{position:absolute;top:22px;color:var(--white);font-size:10px;font-weight:700}
</style>
</head>
<body>
<div class="page">

  <section class="hero" role="img" aria-label="Blurred photo of a white ceramic seal lamp in a vintage shop">
    <div class="hero-title hero-kicker">BRIGHTQUOKKA</div>
    <h1 class="hero-title hero-name">LIGHTBULBS</h1>
    <svg class="slide-arrow prev" width="26" height="86" viewBox="0 0 26 86"><polyline points="25,1 1,43 25,85" fill="none" stroke="#fff" stroke-width="1"/></svg>
    <svg class="slide-arrow next" width="26" height="86" viewBox="0 0 26 86"><polyline points="1,1 25,43 1,85" fill="none" stroke="#fff" stroke-width="1"/></svg>
  </section>

  <header class="topbar">
    <nav class="nav">
      <a href="#" style="left:283px">HOME</a>
      <a href="#" style="left:341px">PRODUCTS</a>
      <a href="#" style="left:423px">SHOPPING</a>
      <a href="#" style="left:505px">CONTACT</a>
    </nav>
    <div class="cart">
      <svg width="18" height="14" viewBox="0 0 18 14"><path d="M1 5h16l-2 8H3z" fill="none" stroke="#fff" stroke-width="1.6"/><path d="M5 5l4-4 4 4" fill="none" stroke="#fff" stroke-width="1.4"/></svg>
      <span>$35.00</span>
      <svg width="8" height="7" viewBox="0 0 8 7" style="margin-left:6px"><path d="M0 0h8L4 7z" fill="#fff"/></svg>
    </div>
  </header>
  <div class="brand-badge">BRIGHTQUOKKA</div>

  <div class="promo promo-quality">
    <div class="photo" role="img" aria-label="Photo of a vintage cartoon cat telephone"></div>
    <div class="copy">SUPER HIGH<br>QUALITY<br>LIGHTBULBS<br><span class="accent">START FROM</span><div class="price">$25.00</div></div>
  </div>
  <div class="promo promo-range">
    <div class="photo" role="img" aria-label="Photo of superhero figurines in a collectibles shop"></div>
    <div class="copy">MORE THAN<br><span class="big">500</span><br>ITEMS<br>AVAILABLE</div>
  </div>

  <section class="contact" role="img" aria-label="Greyscale photo of a cluttered antique shop">
    <div class="contact-glow"></div>
    <h2>CONTACT US</h2>
    <div class="field short" style="left:99px">name ...</div>
    <div class="field short" style="left:285px">email ...</div>
    <div class="field short" style="left:471px">subject ...</div>
    <div class="field message">message ...</div>
    <div class="send">SEND A MESSAGE</div>
  </section>

  <article class="product" style="left:74px"><div class="shot" role="img" aria-label="Photo of a white ceramic seal lamp"></div><p class="name">Curabitur pretium dui.</p><p class="cost">$180.00</p><span class="add"><svg width="14" height="11" viewBox="0 0 18 14"><path d="M1 5h16l-2 8H3z" fill="none" stroke="#fff" stroke-width="2"/><path d="M5 5l4-4 4 4" fill="none" stroke="#fff" stroke-width="1.6"/></svg></span></article>
  <article class="product" style="left:226px"><div class="shot" role="img" aria-label="Photo of a white ceramic seal lamp"></div><p class="name">Curabitur pretium dui.</p><p class="cost">$180.00</p><span class="add"><svg width="14" height="11" viewBox="0 0 18 14"><path d="M1 5h16l-2 8H3z" fill="none" stroke="#fff" stroke-width="2"/><path d="M5 5l4-4 4 4" fill="none" stroke="#fff" stroke-width="1.6"/></svg></span></article>
  <article class="product" style="left:377px"><div class="shot" role="img" aria-label="Photo of a white ceramic seal lamp"></div><p class="name">Curabitur pretium dui.</p><p class="cost">$180.00</p><span class="add"><svg width="14" height="11" viewBox="0 0 18 14"><path d="M1 5h16l-2 8H3z" fill="none" stroke="#fff" stroke-width="2"/><path d="M5 5l4-4 4 4" fill="none" stroke="#fff" stroke-width="1.6"/></svg></span></article>
  <article class="product" style="left:528px"><div class="shot" role="img" aria-label="Photo of a white ceramic seal lamp"></div><p class="name">Curabitur pretium dui.</p><p class="cost">$180.00</p><span class="add"><svg width="14" height="11" viewBox="0 0 18 14"><path d="M1 5h16l-2 8H3z" fill="none" stroke="#fff" stroke-width="2"/><path d="M5 5l4-4 4 4" fill="none" stroke="#fff" stroke-width="1.6"/></svg></span></article>

  <footer class="footer">
    <div class="brand">BRIGHTQUOKKA</div>
    <p class="legal">Copyright © 2013 &nbsp;ALL rights reserved.</p>
    <span class="social" style="left:548px">Share</span>
    <span class="social" style="left:594px">Follow</span>
    <span class="social" style="left:645px">Feed</span>
  </footer>

</div>
</body>
</html>
```